CalmHarbor Homepage and Landing Pages

Please see detailed brief.

CalmHarbor is Australia’s newest online therapy and mental health service. We allow patients from across australia to connect with Mental health practitioners from across Australia. Our mission is to remove the friction in gaining support for mental health related issues.

Number of Pages Required

1 page

Font styles to use
Sans Serif

Colors
33a6d7
0293ce
3277b5
0255a3
acd136
9bcb3c

Requirements
Must have
• Please see detailed brief.
Nice to have
• Please see detailed brief
Should not have

```html
<!DOCTYPE html>
<html lang="en">
<head>
<meta charset="utf-8">
<title>CalmHarbor — Online Therapy &amp; Wellness</title>
<link href="https://fonts.googleapis.com/css2?family=Bebas+Neue&family=Crimson+Text:ital@1&family=Poppins:wght@300;400;500;600;700&display=swap" rel="stylesheet">
<style>
:root{
  --blue:#0293ce;
  --blue-deep:#1a64d6;
  --blue-band:#1c63d9;
  --green:#1ed066;
  --green-dark:#19b758;
  --ink:#111;
  --body:#333;
  --muted:#777;
  --footer:#1d1d1d;
  --white:#fff;
}
*{box-sizing:border-box;margin:0;padding:0}
html,body{width:1200px;height:3399px;overflow:hidden}
body{font-family:"Poppins",sans-serif;color:var(--body);background:var(--white);position:relative}
.abs{position:absolute}
a{color:inherit;text-decoration:none}

/* header */
.top-rule{left:0;top:0;width:1200px;height:2px;background:var(--blue)}
.brand{display:flex;align-items:center;gap:10px;font-weight:300;font-size:34px;color:#2a2a2a;line-height:1}
.brand-dot{width:26px;height:26px;border-radius:50%;background:var(--blue)}
.site-brand{left:235px;top:34px}
.pill{display:flex;align-items:center;justify-content:center;gap:8px;border-radius:20px;color:#fff;font-size:10.5px;font-weight:600;letter-spacing:.2px}
.btn-login{left:703px;top:16px;width:109px;height:37px;background:var(--blue)}
.btn-patient{left:821px;top:16px;width:144px;height:37px;background:var(--green)}
.main-nav{font-size:10.5px;font-weight:600;color:#222}
.main-nav a{position:absolute;white-space:nowrap}
.main-nav .active{color:var(--blue)}

/* hero */
.hero{left:0;top:100px;width:1200px;height:500px;overflow:hidden}
.hero-photo{position:absolute;inset:0;background:linear-gradient(100deg,#6f5a4d 0%,#a48670 35%,#c9ad93 60%,#b59d86 100%)}
.hero-wave{left:0;top:0;width:1200px;height:500px}
.hero-title{left:235px;top:82px;font-family:"Bebas Neue",sans-serif;font-size:46px;color:#fff;letter-spacing:1.5px;line-height:1}
.hero-line{left:235px;top:135px;width:42px;height:2px;background:#fff}
.hero-text{left:235px;top:154px;width:470px;font-size:11px;line-height:18px;color:#fff}
.hero-text p+p{margin-top:17px}
.btn-hero{left:232px;top:248px;width:147px;height:32px;background:var(--blue);border-radius:18px;color:#fff;font-size:10px;font-weight:600;display:flex;align-items:center;justify-content:center}
.dots{display:flex;gap:6px}
.dot{width:12px;height:12px;border-radius:50%;background:var(--green)}
.dot.ring{background:transparent;border:2px solid #fff;position:relative}
.dot.ring::after{content:"";position:absolute;inset:2px;border-radius:50%;background:#fff}
.hero-dots{left:584px;top:352px}

/* about */
.about-mark{left:238px;top:572px;width:84px;height:84px;border-radius:50%;background:var(--blue)}
.about-title{left:235px;top:672px;font-size:19px;font-weight:700;color:var(--blue-deep)}
.about-text{left:235px;top:710px;width:375px;font-size:10.5px;line-height:17.5px;font-weight:600;color:#222}
.ticks{left:235px;top:832px;list-style:none;font-size:10.5px;color:#222}
.ticks li{display:flex;align-items:center;gap:13px;height:30px}
.tick{width:19px;height:19px;border-radius:50%;background:#dcf6e6;display:flex;align-items:center;justify-content:center}
.btn-arrow{display:flex;align-items:center;justify-content:space-between;padding:0 6px 0 20px;height:37px;border-radius:20px;background:var(--green);color:#fff;font-size:10.5px;font-weight:600}
.btn-arrow .circ{width:25px;height:25px;border-radius:50%;background:rgba(255,255,255,.35);display:flex;align-items:center;justify-content:center}
.about-btn{left:235px;top:969px;width:127px}
.about-photo{left:614px;top:594px;width:336px;height:483px;background:linear-gradient(180deg,#e8d9c8 0%,#3d7cc9 45%,#2467b5 100%);border-radius:160px 160px 0 0}

/* booking band */
.booking{left:0;top:1077px;width:1200px;height:413px;background:var(--green)}
.booking h2{position:absolute;left:0;width:1200px;top:58px;text-align:center;color:#fff;font-size:26px;font-weight:700}
.booking .sub{position:absolute;left:0;width:1200px;top:102px;text-align:center;color:#fff;font-size:12.5px;font-weight:600}
.step{top:202px;width:168px;height:131px;background:#fff;text-align:center}
.step .icon{position:absolute;left:51px;top:-30px;width:66px;height:66px;border-radius:50%;background:#fff;border:2px solid var(--green);display:flex;align-items:center;justify-content:center}
.step h3{margin-top:57px;font-size:12.5px;font-weight:600;color:#222}
.step a{display:block;margin-top:17px;font-size:12.5px;color:var(--green);font-weight:500}

/* help */
.help-title{left:235px;top:1598px;font-size:19px;font-weight:700;color:#111}
.rule{height:2px;width:42px;background:var(--blue-deep)}
.help-rule{left:235px;top:1632px}
.help-text{left:235px;top:1662px;width:350px;font-size:10.5px;line-height:16.5px;color:#222}
.help-text p+p{margin-top:16px}
.help-btn{left:235px;top:1806px;width:185px}
.help-photo{left:614px;top:1558px;width:350px;height:404px;background:linear-gradient(180deg,#2e2e34 0%,#4a5b9c 45%,#e6c2a8 100%);border-radius:14px 14px 0 0}

/* testimonial */
.testimonial{left:0;top:1962px;width:1200px;height:462px;background:var(--blue-band)}
.testimonial h2{position:absolute;left:0;width:1200px;top:58px;text-align:center;color:#fff;font-size:26px;font-weight:700}
.testimonial .rule{position:absolute;left:579px;top:107px;background:var(--green)}
.quote-mark{left:567px;top:165px}
.quote{left:310px;top:268px;width:580px;text-align:center;font-family:"Crimson Text",serif;font-style:italic;font-size:12.5px;line-height:18.5px;color:#fff}
.quote-name{left:0;width:1200px;top:346px;text-align:center;font-size:10.5px;font-weight:600;color:#fff}
.t-dots{left:584px;top:391px}
.arrow-l{left:152px;top:284px}
.arrow-r{left:1018px;top:284px}

/* team */
.team-title{left:0;width:1200px;top:2492px;text-align:center;font-size:25px;font-weight:700;color:#111}
.team-rule{left:579px;top:2540px}
.team-text{left:235px;top:2612px;width:350px;font-size:10px;line-height:15.8px;color:#222}
.team-text p+p{margin-top:14px}
.team-btn{left:235px;top:2961px;width:127px}
.team-photo{left:610px;top:2608px;width:590px;height:473px;background:radial-gradient(ellipse at 70% 40%,#4a4038 0%,#1e1b19 45%,#050505 75%)}
.team-name{left:648px;top:2798px;font-size:21px;font-weight:700;color:var(--green)}
.team-role{left:648px;top:2830px;font-size:11.5px;color:#fff}

/* footer */
.footer{left:0;top:3081px;width:1200px;height:318px;background:var(--footer)}
.footer .brand{color:#fff;position:absolute;left:235px;top:62px}
.footer-about{left:235px;top:113px;width:200px;font-size:10.5px;line-height:16px;color:#bbb}
.f-head{font-size:11.5px;font-weight:700;color:#fff}
.f-rule{position:absolute;height:2px;width:42px;background:var(--blue-deep)}
.f-links{list-style:none;font-size:10.5px;color:#bbb}
.f-links li{height:22.5px;display:flex;gap:7px}
.f-links li::before{content:"›";color:var(--green)}
.news-text{left:770px;top:106px;font-size:9px;line-height:17px;color:#bbb}
.news-input{left:770px;top:156px;width:194px;height:28px;background:#fff;border-radius:15px;display:flex;align-items:center;padding-left:12px;gap:6px;font-size:9px;color:#888}
.news-send{position:absolute;right:4px;top:3px;width:22px;height:22px;border-radius:50%;background:var(--green);display:flex;align-items:center;justify-content:center}
.f-divider{left:235px;top:248px;width:730px;height:1px;background:#333}
.copy{left:235px;top:276px;font-size:9px;color:#888}
.copy b{color:var(--green);font-weight:500}
.legal{left:806px;top:276px;font-size:9px;color:#888}
</style>
</head>
<body>

<header>
  <div class="abs top-rule"></div>
  <div class="abs brand site-brand"><span class="brand-dot"></span>CalmHarbor</div>
  <a class="abs pill btn-login" href="#">
    <svg width="14" height="14" viewBox="0 0 14 14" fill="none" stroke="#fff" stroke-width="1.3"><path d="M6 2h6v10H6M1 7h7M5.5 4.5 8 7l-2.5 2.5"/></svg>LOGIN IN</a>
  <a class="abs pill btn-patient" href="#">
    <svg width="14" height="14" viewBox="0 0 14 14" fill="none" stroke="#fff" stroke-width="1.3"><circle cx="7" cy="4.5" r="3"/><path d="M1.5 13c0-3 2.5-5 5.5-5s5.5 2 5.5 5"/></svg>PATIENT SIGN IN</a>
  <nav class="abs main-nav" style="left:0;top:72px">
    <a class="active" style="left:574px">HOME</a>
    <a style="left:638px">ABOUT US</a>
    <a style="left:722px">PRACTITIONER</a>
    <a style="left:829px">OUR TEAM</a>
    <a style="left:914px">CONTACT</a>
  </nav>
</header>

<section class="abs hero">
  <div class="hero-photo" role="img" aria-label="Photo of a smiling couple embracing"></div>
  <svg class="abs hero-wave" viewBox="0 0 1200 500" aria-hidden="true">
    <path d="M0,385 C120,338 260,330 420,365 C560,398 650,478 780,472 C950,466 1100,445 1200,408 L1200,500 L0,500 Z" fill="#fff"/>
    <path d="M0,385 C120,338 260,330 420,365 C560,398 650,478 780,472 C950,466 1100,445 1200,408" fill="none" stroke="#1ed066" stroke-width="9"/>
  </svg>
  <h1 class="abs hero-title">WELCOME TO CALMHARBOR</h1>
  <div class="abs hero-line"></div>
  <div class="abs hero-text">
    <p>CalmHarbor provides on-demand access to a range of psychologists &amp; personal wellness professionals from across Australia.</p>
    <p>Book your online appointment in minutes, 24/7.</p>
  </div>
  <a class="abs btn-hero" href="#">FIND A PRACTITIONER</a>
  <div class="abs dots hero-dots"><span class="dot"></span><span class="dot ring"></span></div>
</section>

<section class="about">
  <div class="abs about-mark"></div>
  <h2 class="abs about-title">ABOUT US</h2>
  <p class="abs about-text">Lorem ipsum dolor sit amet, consectetur adipiscing elit. Donec vitae lacus sit amet orci tristique vulputate sit amet ut dui. Mauris vel odio convallis est semper vulputate. Maecenas rhoncus, ante ut aliquet pretium, lectus purus fringilla ex, a gravida urna arcu id leo. Integer nec eros erat. Maecenas lobortis convallis diam, mollis ultricies sapien sodales nec.</p>
  <ul class="abs ticks">
    <li><span class="tick"><svg width="9" height="9" viewBox="0 0 10 10" fill="none" stroke="#1ed066" stroke-width="1.8"><path d="M1.5 5.2 4 7.5 8.5 2.5"/></svg></span>In ultricies justo ut rutrum varius. Integer sed suscipit diam.</li>
    <li><span class="tick"><svg width="9" height="9" viewBox="0 0 10 10" fill="none" stroke="#1ed066" stroke-width="1.8"><path d="M1.5 5.2 4 7.5 8.5 2.5"/></svg></span>Quisque tincidunt hendrerit diam in euismod.</li>
    <li><span class="tick"><svg width="9" height="9" viewBox="0 0 10 10" fill="none" stroke="#1ed066" stroke-width="1.8"><path d="M1.5 5.2 4 7.5 8.5 2.5"/></svg></span>Nam porta sem eros, dapibus tempus risus tristique ut.</li>
    <li><span class="tick"><svg width="9" height="9" viewBox="0 0 10 10" fill="none" stroke="#1ed066" stroke-width="1.8"><path d="M1.5 5.2 4 7.5 8.5 2.5"/></svg></span>Vestibulum ante ipsum primis in faucibus orci luctus et.</li>
  </ul>
  <a class="abs btn-arrow about-btn" href="#">LEARN MORE<span class="circ"><svg width="8" height="10" viewBox="0 0 8 10" fill="none" stroke="#fff" stroke-width="1.6"><path d="M2 1l4 4-4 4"/></svg></span></a>
  <div class="abs about-photo" role="img" aria-label="Photo of a smiling practitioner in blue scrubs giving thumbs up"></div>
</section>

<section class="abs booking">
  <h2>Find a Doctors and Book appointments online instantly!</h2>
  <p class="sub">Choose the best time for you. Book with a click.</p>
  <div class="abs step" style="left:235px">
    <span class="icon"><svg width="32" height="32" viewBox="0 0 32 32" fill="none" stroke="#1ed066" stroke-width="1.6"><circle cx="14" cy="14" r="9"/><path d="M21 21l7 7M14 10v8M10 14h8"/></svg></span>
    <h3>Search Doctor, 24/7</h3><a href="#">More Info</a></div>
  <div class="abs step" style="left:422px">
    <span class="icon"><svg width="32" height="32" viewBox="0 0 32 32" fill="none" stroke="#1ed066" stroke-width="1.6"><circle cx="16" cy="9" r="4"/><path d="M9 22c0-4 3-7 7-7s7 3 7 7M4 27h24"/><circle cx="7" cy="15" r="2.5"/><circle cx="25" cy="15" r="2.5"/></svg></span>
    <h3>Choose Best Practice</h3><a href="#">More Info</a></div>
  <div class="abs step" style="left:610px">
    <span class="icon"><svg width="32" height="32" viewBox="0 0 32 32" fill="none" stroke="#1ed066" stroke-width="1.6"><rect x="4" y="7" width="24" height="21" rx="2"/><path d="M4 13h24M10 4v6M22 4v6M9 18h3M15 18h3M21 18h3M9 23h3M15 23h3"/></svg></span>
    <h3>Book Appointment</h3><a href="#">More Info</a></div>
  <div class="abs step" style="left:797px">
    <span class="icon"><svg width="32" height="32" viewBox="0 0 32 32" fill="none" stroke="#1ed066" stroke-width="1.6"><circle cx="13" cy="10" r="5"/><path d="M3 28c0-6 4-10 10-10 3 0 5 1 7 2"/><rect x="19" y="20" width="10" height="8" rx="1"/><path d="M21.5 24l2 2 3-3.5"/></svg></span>
    <h3>Review Service</h3><a href="#">More Info</a></div>
</section>

<section class="help">
  <h2 class="abs help-title">Find the help you need</h2>
  <div class="abs rule help-rule"></div>
  <div class="abs help-text">
    <p>Book an appointment with one of our highly qualified, licensed practitioners.</p>
    <p>The consultation can be conducted from wherever you feel most comfortable.</p>
    <p>No travel. No Clinics.</p>
  </div>
  <a class="abs btn-arrow help-btn" href="#">FIND A PRACTITIONER<span class="circ"><svg width="8" height="10" viewBox="0 0 8 10" fill="none" stroke="#fff" stroke-width="1.6"><path d="M2 1l4 4-4 4"/></svg></span></a>
  <div class="abs help-photo" role="img" aria-label="Photo of hands holding a tablet showing a practitioner search page"></div>
</section>

<section class="abs testimonial" role="img" aria-label="Blue-tinted grid of portrait photos behind a client testimonial">
  <h2>Testimonial</h2>
  <div class="rule"></div>
  <svg class="abs quote-mark" width="62" height="48" viewBox="0 0 66 52" aria-hidden="true"><path d="M0 52V28C0 12 7 3 22 0l3 7c-8 3-11 8-11 15h14v30zM38 52V28C38 12 45 3 60 0l3 7c-8 3-11 8-11 15h14v30z" fill="#1ed066"/></svg>
  <svg class="abs arrow-l" width="30" height="14" viewBox="0 0 30 14" aria-hidden="true"><path d="M30 7H4M9 1 2 7l7 6" fill="none" stroke="#1ed066" stroke-width="3"/></svg>
  <svg class="abs arrow-r" width="30" height="14" viewBox="0 0 30 14" aria-hidden="true"><path d="M0 7h26M21 1l7 6-7 6" fill="none" stroke="#1ed066" stroke-width="3"/></svg>
  <p class="abs quote">Lorem ipsum dolor sit amet, consectetur adipiscing elit. Curabitur et bibendum augue, at fermentum tellus. Suspendisse aliquam ac elit eu blandit. Pellentesque habitant morbi tristique senectus et netus et malesuada fames ac turpis egestas. Praesent vel urna facilisis, lacinia mi nec, ornare lorem.</p>
  <p class="abs quote-name">LIAM CARVER</p>
  <div class="abs dots t-dots"><span class="dot" style="background:#fff"></span><span class="dot" style="background:transparent;border:2px solid #1ed066"></span></div>
</section>

<section class="team">
  <h2 class="abs team-title">Meet Our Team</h2>
  <div class="abs rule team-rule"></div>
  <div class="abs team-text">
    <p>Dr Neil Harrow is an Australian neuroscientist in private practice specializing in brain performance. He has a bachelor's degree in psychology and a doctorate of science in biological statistics. Dr Harrow has worked as a psychologist for over 30 years and more recently has focused on the neurosciences.</p>
    <p>Neil has helped many people, schools, sporting teams and organisations with improving performance and in particular memory, concentration, agility and resilience. It was through the discovery of the positive neurological effects of colouring-in using Dr Harrow's designs which has sparked a worldwide sensation resulting in three of Dr Harrow's colouring-in brain science books being featured by Marla Quinn in her 2016 Christmas Wish List.</p>
    <p>His current work as CEO and Chief neuroscientist for The Mind Lab (has led to his development of innovative technologies and programmes across Australia and internationally for individuals (brain coaching), peak performance sport teams (pro leagues) and companies listed in the world's top 500 looking for creative brain based initiatives to facilitate corporate success.</p>
  </div>
  <a class="abs btn-arrow team-btn" href="#">LEARN MORE<span class="circ"><svg width="8" height="10" viewBox="0 0 8 10" fill="none" stroke="#fff" stroke-width="1.6"><path d="M2 1l4 4-4 4"/></svg></span></a>
  <div class="abs team-photo" role="img" aria-label="Portrait photo of the chief science advisor against a black background"></div>
  <h3 class="abs team-name">Dr. Neil Harrow</h3>
  <p class="abs team-role">Neuroscientist &amp; Chief Science Advisor</p>
</section>

<footer class="abs footer">
  <div class="brand"><span class="brand-dot"></span>CalmHarbor</div>
  <p class="abs footer-about">Lorem ipsum dolor sit amet, consectetur adipiscing elit. Curabitur et bibendum augue, at fermentum tellus. Suspendisse aliquam ac elit eu blandit. Pellentesque habitant morbi tristique.</p>

  <h4 class="abs f-head" style="left:473px;top:52px">QUICK LINKS</h4>
  <span class="f-rule" style="left:473px;top:77px"></span>
  <ul class="abs f-links" style="left:477px;top:106px"><li>Home</li><li>About Us</li><li>Practitioner</li><li>Our Team</li><li>Contact</li></ul>

  <h4 class="abs f-head" style="left:598px;top:52px">FOLLOW US</h4>
  <span class="f-rule" style="left:598px;top:77px"></span>
  <ul class="abs f-links" style="left:602px;top:106px"><li>Gatherly</li><li>Chirpline</li><li>Workmesh</li><li>Reelhub</li></ul>

  <h4 class="abs f-head" style="left:770px;top:52px">NEWSLETTER</h4>
  <span class="f-rule" style="left:770px;top:77px"></span>
  <p class="abs news-text">Subscribe to get updates right in your inbox.<br>We promise to not send you spams.</p>
  <div class="abs news-input">
    <svg width="11" height="8" viewBox="0 0 11 8" fill="none" stroke="#888"><rect x=".5" y=".5" width="10" height="7"/><path d="M.5.5l5 4 5-4"/></svg>Enter email here
    <span class="news-send"><svg width="10" height="10" viewBox="0 0 10 10"><path d="M0 4.5 10 0 7 10 5 6z" fill="#fff"/></svg></span>
  </div>

  <div class="abs f-divider"></div>
  <p class="abs copy">Copyright © 2020 <b>CalmHarbor</b>. All Right Reserved.</p>
  <p class="abs legal">Terms &amp; Condition &nbsp;| &nbsp;&nbsp;&nbsp;Privacy Policy</p>
</footer>

</body>
</html>
```